Tidal Sparks - Main Menu - Re-Design

I want to have a refresh for this app's main menu. There are some different items on the menu depending on the language (English vs. Non-English) and version (Pro vs. Free). I have attached screenshots of the different conditions. This app is a collection of brain training games.

Need designs for light and dark mode. Need designs for both portrait and landscape mode.

Here is a link to the app in Brisk Market.
https://apps.briskmarket.example/store/apps/details?id=tidalworks.tidalsparks

Here is a link to the app in the Orvel App Store.
https://depot.orvel.example/us/app/tidal-sparks-focus-drills/id519274063?ls=1&mt=8

```html
<!DOCTYPE html>
<html lang="en">
<head>
<meta charset="utf-8">
<title>Tidal Sparks – Main Menu</title>
<link rel="stylesheet" href="https://fonts.googleapis.com/css2?family=Josefin+Sans:wght@400&family=Josefin+Slab:wght@600&display=swap">
<style>
  :root {
    --stage: #8e8e8e;
    --navy: #07122b;
    --navy-deep: #040a1c;
    --orange: #e0521a;
    --blue: #2a62d4;
    --gold: #f2a31b;
    --cream: #f4f1dd;
    --tile: #ffffff;
    --tile-edge: #dedbd0;
    --ink: #1b1b1b;
    --mark: #1f6fe0;
  }
  * { box-sizing: border-box; margin: 0; padding: 0; }
  html, body { width: 1200px; height: 951px; overflow: hidden; }
  body { background: var(--stage); position: relative; font-family: "Josefin Slab", serif; }

  .screen { position: absolute; overflow: hidden; }

  /* splash */
  .splash {
    left: 83px; top: 102px; width: 314px; height: 680px; border-radius: 34px;
    background: linear-gradient(180deg, var(--navy-deep) 0%, var(--navy) 100%);
    text-align: center;
  }
  .splash-mark {
    position: absolute; left: 94px; top: 22px; width: 126px; height: 126px;
    border-radius: 50%; background: var(--mark);
  }
  .splash-title {
    position: absolute; left: 0; right: 0; top: 206px;
    font-family: "Josefin Sans", sans-serif; font-weight: 400;
    color: #fff; font-size: 45px; line-height: 55px;
  }
  .splash-tagline {
    position: absolute; left: 0; right: 0; top: 334px;
    font-size: 43px; line-height: 55px;
  }
  .splash-tagline .accent-orange { color: var(--orange); display: block; }
  .splash-tagline .accent-blue { color: var(--blue); display: block; }
  .splash-art {
    position: absolute; left: 0; right: 0; top: 475px; bottom: 0;
    background: radial-gradient(ellipse 60% 45% at 50% 55%, #2f7de8 0%, #173c93 45%, var(--navy) 80%);
  }

  /* headers */
  .app-header {
    position: absolute; left: 0; top: 0; width: 100%; height: 89px;
    background: var(--navy);
  }
  .header-mark { position: absolute; top: 16px; width: 58px; height: 58px; border-radius: 50%; background: var(--mark); }
  .greeting {
    position: absolute; top: 31px; font-size: 22px; white-space: nowrap;
    color: var(--orange); transform: translateX(-50%);
  }
  .greeting .name { color: var(--blue); }
  .gear { position: absolute; top: 30px; width: 30px; height: 30px; }

  /* portrait */
  .portrait { left: 443px; top: 81px; width: 338px; height: 789px; background: var(--cream); }
  .portrait .header-mark { left: 23px; }
  .portrait .greeting { left: 185px; }
  .portrait .gear { left: 285px; }
  .portrait .menu-grid {
    position: absolute; left: 10px; top: 100px;
    display: grid; grid-template-columns: 153px 153px; grid-auto-rows: 129px; gap: 11px;
  }
  .portrait .tile-icon { width: 60px; height: 60px; margin-bottom: 8px; }
  .portrait .tile-label { font-size: 18px; line-height: 20px; }
  .portrait-art {
    position: absolute; left: 0; right: 0; top: 531px; bottom: 0;
    background:
      radial-gradient(ellipse 42% 40% at 52% 38%, #d23c6f 0%, #6a4bb8 45%, rgba(244,241,221,0) 75%),
      linear-gradient(0deg, #e8c33a 0%, #36a676 7%, var(--cream) 20%);
  }

  /* landscape */
  .landscape {
    left: 804px; top: 81px; width: 338px; height: 333px;
    background: radial-gradient(ellipse 70% 60% at 55% 60%, #6d2bb5 0%, #2b1a8a 45%, #10124a 100%);
  }
  .landscape .gear { left: 22px; }
  .landscape .greeting { left: 152px; }
  .landscape .header-mark { left: 257px; }
  .landscape .menu-grid {
    position: absolute; left: 8px; top: 120px;
    display: grid; grid-template-columns: repeat(3, 103px); grid-auto-rows: 86px; gap: 7px 7px;
  }
  .landscape .tile-icon { width: 36px; height: 36px; margin-bottom: 5px; }
  .landscape .tile-label { font-size: 12px; line-height: 13px; font-weight: 600; }

  /* tiles */
  .menu-tile {
    background: var(--tile); border: 2px solid var(--tile-edge); border-radius: 6px;
    display: flex; flex-direction: column; align-items: center; justify-content: center;
    text-align: center; color: var(--ink);
  }
  .tile-icon { border-radius: 10px; }
  .icon-brain { background: linear-gradient(135deg, #f7a3a8, #e0707a); }
  .icon-games { background: linear-gradient(135deg, #f7c63b, #e09a16); }
  .icon-learning { background: linear-gradient(135deg, #e0445a, #8a5a3c); }
  .icon-about { background: linear-gradient(135deg, #f39b3a, #f6c66b); }
  .icon-schedule { background: linear-gradient(135deg, #e54d4d, #cfd6dc); }
  .icon-scores { background: linear-gradient(90deg, #39c25a, #f4c430, #ee5a3a); }
</style>
</head>
<body>

<section class="screen splash">
  <div class="splash-mark"></div>
  <h1 class="splash-title">TIDAL<br>SPARKS PRO</h1>
  <p class="splash-tagline"><span class="accent-orange">Exercise Your</span><span class="accent-blue">Brain</span></p>
  <div class="splash-art" role="img" aria-label="Glowing blue digital brain illustration"></div>
</section>

<section class="screen portrait">
  <header class="app-header">
    <div class="header-mark"></div>
    <p class="greeting">Welcome <span class="name">Guest</span></p>
    <svg class="gear" viewBox="0 0 30 30" aria-label="Settings">
      <g fill="var(--gold)">
        <circle cx="15" cy="15" r="10"/>
        <rect x="12" y="1" width="6" height="28" rx="1.5"/>
        <rect x="12" y="1" width="6" height="28" rx="1.5" transform="rotate(45 15 15)"/>
        <rect x="12" y="1" width="6" height="28" rx="1.5" transform="rotate(90 15 15)"/>
        <rect x="12" y="1" width="6" height="28" rx="1.5" transform="rotate(135 15 15)"/>
      </g>
      <circle cx="15" cy="15" r="4.5" fill="var(--navy)"/>
    </svg>
  </header>
  <nav class="menu-grid">
    <div class="menu-tile"><div class="tile-icon icon-brain" role="img" aria-label="Brain icon"></div><span class="tile-label">Training<br>Center</span></div>
    <div class="menu-tile"><div class="tile-icon icon-games" role="img" aria-label="Game controller icon"></div><span class="tile-label">Games<br>List</span></div>
    <div class="menu-tile"><div class="tile-icon icon-learning" role="img" aria-label="Open book with brain icon"></div><span class="tile-label">Learning</span></div>
    <div class="menu-tile"><div class="tile-icon icon-about" role="img" aria-label="Head lifting weights icon"></div><span class="tile-label">About</span></div>
    <div class="menu-tile"><div class="tile-icon icon-schedule" role="img" aria-label="Calendar with clock icon"></div><span class="tile-label">Schedule</span></div>
    <div class="menu-tile"><div class="tile-icon icon-scores" role="img" aria-label="Score bars icon"></div><span class="tile-label">Scores</span></div>
  </nav>
  <div class="portrait-art" role="img" aria-label="Colourful low-poly mosaic brain illustration"></div>
</section>

<section class="screen landscape" role="img" aria-label="Neon purple abstract background">
  <header class="app-header">
    <svg class="gear" viewBox="0 0 30 30" aria-label="Settings">
      <g fill="var(--gold)">
        <circle cx="15" cy="15" r="10"/>
        <rect x="12" y="1" width="6" height="28" rx="1.5"/>
        <rect x="12" y="1" width="6" height="28" rx="1.5" transform="rotate(45 15 15)"/>
        <rect x="12" y="1" width="6" height="28" rx="1.5" transform="rotate(90 15 15)"/>
        <rect x="12" y="1" width="6" height="28" rx="1.5" transform="rotate(135 15 15)"/>
      </g>
      <circle cx="15" cy="15" r="4.5" fill="var(--navy)"/>
    </svg>
    <p class="greeting">Welcome <span class="name">Guest</span></p>
    <div class="header-mark"></div>
  </header>
  <nav class="menu-grid">
    <div class="menu-tile"><div class="tile-icon icon-brain" role="img" aria-label="Brain icon"></div><span class="tile-label">Training<br>Center</span></div>
    <div class="menu-tile"><div class="tile-icon icon-learning" role="img" aria-label="Open book with brain icon"></div><span class="tile-label">Learning</span></div>
    <div class="menu-tile"><div class="tile-icon icon-schedule" role="img" aria-label="Calendar with clock icon"></div><span class="tile-label">Schedule</span></div>
    <div class="menu-tile"><div class="tile-icon icon-games" role="img" aria-label="Game controller icon"></div><span class="tile-label">Games<br>List</span></div>
    <div class="menu-tile"><div class="tile-icon icon-about" role="img" aria-label="Head lifting weights icon"></div><span class="tile-label">About</span></div>
    <div class="menu-tile"><div class="tile-icon icon-scores" role="img" aria-label="Score bars icon"></div><span class="tile-label">Scores</span></div>
  </nav>
</section>

</body>
</html>
```